Wordpress design for my private practice website - Psychotherapist

I would like a simple, clean, and elegant design for my private practice website. I work with both adults and children so I'd like it to appeal to both. However, since parents make the choice as to where to send their child for therapy, I want it to appeal to adults more. I would like the pictures on the site to have a calming effect - maybe using sand and water and rocks. I am attaching files with my company logo. I would also like my name incorporated into the header - Colette Brannigan, LCSW, Registered Play Therapist. I've also uploaded a picture of myself for my About Page.

I like the design of these 2 website and want something similar:
www.drlorapenwick.example
www.harwood-tallis.example

I would like a home page that highlights a calming graphic across the entire top of the page as well as my practice logo and my name.

I'd like a link to social media sites on the top of the homepage - facebook, pinterest.

I want a simple bar across the top with the following tabs:
Home
About Me (subtabs Who I Am, Specialties and Approach)
Counseling Services (subtabs Individual Counseling, Play Therapy, Sandplay Therapy,)
Fees
FAQs
Contact Me (would love this to be a fill in the blank contact form that sends info to my email address - should include name, phone number, email and a comment box for more information requested)
Blog (this will link with another wordpress blog)

Target Market(s)

Parents of children under age 12 with behavioral problems or are dealing with the breakup of their family through divorce - looking for someone to work with their young child. I also work with Adults that are overwhelmed and worried - often women that have many life stressors and are feeling burnt out on life and meeting everyone's needs. Families going through some type of trauma, including divorce or grief work. I also work with individuals going through a transition of religious beliefs - often exiting the religion of their youth and undergoing a crisis of faith at midlife.

Industry/Entity Type

Mental Health

Contact Information for Business Card

Colette Brannigan, LCSW
Registered Play Therapist
4917 Wexmoor Lane
Idaho Falls, Idaho 83404
(208)555-0187
www.stillbrookcounseling.example

On the opposite side, I'd like an appointment reminder area - with the following text:

Your next appointment is
_____/______/______ at ______am/pm
Please give 24 hrs notice if you need to cancel your appointment.

Coding

Coded - Design and coding required

Number of Pages Required

5+ page

Font styles to use
Sans Serif

Colors
33a6d7
9bcb3c
0355a3

Requirements
Must have
• I'd like it to be a wordpress site. I'm such a newby at web design - but I need to be able to add content and manage the site myself once it is up and running.
Nice to have
• I like the design of these 2 websites and want something similar:
• www.drlorapenwick.example
• www.harwood-tallis.example
• They are clean, easy to navigate and calming.
Should not have
• Should not look like a childcare website.

```html
<!DOCTYPE html>
<html lang="en">
<head>
<meta charset="utf-8">
<title>Stillbrook Counseling – About</title>
<link rel="stylesheet" href="https://fonts.googleapis.com/css2?family=Open+Sans:wght@300;400;600&family=EB+Garamond:wght@600&family=Dancing+Script:wght@700&display=swap">
<style>
  :root {
    --white: #ffffff;
    --ink: #5e5e5e;
    --ink-soft: #6a6a6a;
    --ink-faint: #8a8a8a;
    --brand-navy: #1e4f7f;
    --stone-dark: #5d5852;
    --stone-grey: #8f8c88;
    --stone-light: #aaa59d;
    --stone-blue: #8e949a;
    --stone-tan: #b88e5c;
    --stone-ochre: #c49a5a;
    --nav-top: #fafafa;
    --nav-bottom: #ececec;
    --content-bg: #edecec;
    --dropdown: #6e6e6e;
    --dropdown-line: #8c8c8c;
    --frame: #cfcfcf;
    --grass-light: #ecdca0;
    --grass-mid: #d8bf78;
    --grass-deep: #b9a060;
    --knit-green: #7d8f4c;
    --footer-bg: #f1f0f0;
    --footer-dot: #dcdcdc;
  }
  * { box-sizing: border-box; margin: 0; padding: 0; }
  html, body { width: 1200px; height: 1148px; overflow: hidden; }
  body {
    position: relative;
    background: var(--white);
    font-family: "Open Sans", Arial, sans-serif;
    color: var(--ink);
  }

  .site-header {
    position: absolute; left: 0; top: 0; width: 1200px; height: 144px;
    display: flex; flex-direction: column; align-items: center; justify-content: center;
  }
  .brand-mark {
    width: 40px; height: 40px; border-radius: 50%;
    background: var(--brand-navy); margin-bottom: 14px;
  }
  .brand-name {
    font-size: 16px; font-weight: 400; letter-spacing: 4.5px;
    color: var(--ink-soft); text-transform: uppercase; line-height: 1.2;
  }
  .brand-sub {
    font-size: 8px; font-weight: 600; letter-spacing: 3px;
    color: var(--ink-soft); text-transform: uppercase; margin-top: 5px;
  }

  .hero {
    position: absolute; left: 0; top: 144px; width: 1200px; height: 335px;
    background:
      radial-gradient(ellipse 260px 120px at 28% 58%, var(--stone-light) 0%, transparent 100%),
      radial-gradient(ellipse 140px 120px at 55% 30%, var(--stone-light) 0%, transparent 100%),
      radial-gradient(ellipse 150px 110px at 58% 70%, var(--stone-blue) 0%, transparent 100%),
      radial-gradient(ellipse 120px 90px at 77% 22%, var(--stone-light) 0%, transparent 100%),
      radial-gradient(ellipse 130px 100px at 75% 52%, var(--stone-tan) 0%, transparent 100%),
      radial-gradient(ellipse 230px 170px at 92% 85%, var(--stone-ochre) 0%, transparent 100%),
      radial-gradient(ellipse 120px 90px at 6% 60%, var(--stone-tan) 0%, transparent 100%),
      radial-gradient(ellipse 90px 60px at 45% 98%, var(--stone-ochre) 0%, transparent 100%),
      linear-gradient(160deg, var(--stone-dark) 0%, var(--stone-grey) 45%, var(--stone-dark) 100%);
  }
  .hero-title {
    position: absolute; left: 199px; top: 167px;
    font-family: "EB Garamond", Georgia, serif; font-weight: 600;
    font-size: 28px; color: var(--white); line-height: 1;
    text-shadow: 0 1px 3px rgba(0,0,0,0.35);
  }
  .hero-role {
    position: absolute; left: 200px; top: 198px;
    font-family: "Dancing Script", cursive; font-weight: 700;
    font-size: 17px; color: var(--white); line-height: 1;
    text-shadow: 0 1px 3px rgba(0,0,0,0.35);
  }
  .hero-social {
    position: absolute; left: 1048px; top: 52px;
    display: flex; gap: 11px;
  }
  .hero-social span {
    width: 12px; height: 12px; border-radius: 50%; background: var(--white);
  }

  .main-nav {
    position: absolute; left: 0; top: 479px; width: 1200px; height: 76px;
    background: linear-gradient(var(--nav-top), var(--nav-bottom));
    box-shadow: 0 2px 3px rgba(0,0,0,0.08);
    z-index: 2;
  }
  .main-nav a {
    position: absolute; top: 31px;
    font-size: 15px; color: var(--ink); text-decoration: none; line-height: 1;
  }
  .main-nav .has-sub::after {
    content: ""; display: inline-block; width: 5px; height: 5px;
    border-right: 1px solid var(--ink-faint); border-bottom: 1px solid var(--ink-faint);
    transform: rotate(45deg); margin-left: 5px; vertical-align: 3px;
  }

  .content {
    position: absolute; left: 0; top: 578px; width: 1200px; height: 445px;
    background: var(--content-bg);
  }

  .submenu {
    position: absolute; left: 338px; top: 555px; width: 133px;
    background: var(--dropdown); z-index: 3; list-style: none;
  }
  .submenu li {
    color: var(--white); font-size: 13px; font-weight: 300; text-transform: uppercase; line-height: 22px;
  }
  .submenu .who { height: 44px; padding-top: 13px; text-align: center; border-bottom: 1px solid var(--dropdown-line); }
  .submenu .approach { padding: 6px 8px 9px 15px; }

  .portrait {
    position: absolute; left: 83px; top: 652px; width: 339px; height: 335px;
    border: 4px solid var(--frame);
    background:
      radial-gradient(ellipse 140px 60px at 50% 100%, var(--knit-green) 0%, transparent 100%),
      radial-gradient(ellipse 160px 200px at 50% 45%, var(--grass-mid) 0%, transparent 100%),
      linear-gradient(180deg, var(--grass-light) 0%, var(--grass-mid) 60%, var(--grass-deep) 100%);
  }

  .about-title {
    position: absolute; left: 445px; top: 616px; width: 660px; text-align: center;
    font-size: 26px; font-weight: 600; color: var(--ink-soft); letter-spacing: 0.5px;
  }
  .about-text {
    position: absolute; left: 445px; width: 662px;
    font-size: 12.3px; font-weight: 300; line-height: 21px; color: var(--ink);
  }
  .about-text.first { top: 674px; }
  .about-text.second { top: 864px; }

  .footer-band {
    position: absolute; left: 0; top: 1023px; width: 1200px; height: 22px;
    background: #f9f8f8; border-top: 4px solid #e4e3e3; border-bottom: 1px solid #e6e5e5;
  }
  .site-footer {
    position: absolute; left: 0; top: 1045px; width: 1200px; height: 103px;
    background: var(--footer-bg); text-align: center;
  }
  .copyright {
    margin-top: 22px; font-size: 12.5px; font-weight: 300; color: var(--ink-faint);
  }
  .footer-social {
    display: flex; justify-content: center; gap: 9px; margin-top: 13px;
  }
  .footer-social span {
    width: 22px; height: 22px; border-radius: 50%; background: var(--footer-dot);
  }
</style>
</head>
<body>
  <header class="site-header">
    <div class="brand-mark"></div>
    <div class="brand-name">Stillbrook</div>
    <div class="brand-sub">Counseling</div>
  </header>

  <section class="hero" role="img" aria-label="Banner photograph of smooth grey and tan river stones">
    <div class="hero-social" aria-label="Social links"><span></span><span></span><span></span></div>
    <h1 class="hero-title">Colette Brannigan,</h1>
    <p class="hero-role">Relationship Counselor</p>
  </section>

  <nav class="main-nav">
    <a class="has-sub" style="left:303px">Home</a>
    <a style="left:383px">About</a>
    <a class="has-sub" style="left:463px">Counseling Services</a>
    <a style="left:632px">Fees</a>
    <a style="left:702px">FAQs</a>
    <a style="left:776px">Contact</a>
    <a style="left:867px">Blog</a>
  </nav>

  <main class="content"></main>

  <ul class="submenu">
    <li class="who">Who I Am</li>
    <li class="approach">Specialities and Approach</li>
  </ul>

  <div class="portrait" role="img" aria-label="Portrait photograph of the counselor outdoors in golden grass"></div>

  <h2 class="about-title">ABOUT</h2>
  <p class="about-text first">Lorem ipsum dolor sit amet, consectetur adipiscing elit. Quisque nec tempor nunc. Proin vestibulum lacinia metus, vitae efficitur est luctus sed. Etiam neque felis, ullamcorper eu urna quis, consectetur pulvinar tortor. Vestibulum ullamcor­per semper nisi, pretium molestie tortor scelerisque eu. Phasellus quis leo id leo tempus rutrum in eu massa. Ut felis nulla, dapibus id malesuada et, sodales eget velit. Aenean facilisis arcu quis pellentesque rhoncus. Nunc tempus ex vitae arcu sodales, eu efficitur est luctus. Nullam dolor leo, ornare vel faucibus vel, porta vel est. Phasellus at mauris id nunc mattis commodo vitae eget elit. Quisque et gravida nisi. Pellentesque sagittis mauris et iaculis volutpat. Ut vehicula a libero ultricies mattis. Ut cursus ligula auctor, vestibulum dolor eget, lobortis nibh. Fusce molestie volutpat interdum.</p>
  <p class="about-text second">Nunc tempus ex vitae arcu sodales, eu efficitur est luctus. Nullam dolor leo, ornare vel faucibus vel, porta vel est. Pha­sellus at mauris id nunc mattis commodo vitae eget elit. Quisque et gravida nisi. Pellentesque sagittis mauris et iaculis volutpat.</p>

  <div class="footer-band"></div>
  <footer class="site-footer">
    <p class="copyright">© 2012 Colette Brannigan. All rights reserved.</p>
    <div class="footer-social" aria-label="Social links"><span></span><span></span><span></span><span></span></div>
  </footer>
</body>
</html>
```